Attractive door board for entrance beautysalon

Make an attractive design for a board that can be glued on the front door of a beauty salon. The salon location has no window in the front so I need something catchy and attractive. The door board contains a list of the services and the website: www.atelierkm.be, and the text "Enkel op afspraak, bel 0486317492"

Target Market(s)

woman between 16 and 99 years old

Industry/Entity Type

Beauty Salon

Font styles to use
Sans Serif

Requirements
Must have
• A very nice, attractive but sober design.
• It must have a classy Morvane, Lusa, ... chique design.
• The logo must be on it (in attachment)
• There must be the following list in it:
• Gelaatsverzorging
• Wimperverlenging
• Wimperlifting
• Suikerontharing
• Permanente Make Up
• Airbrush Tanning
• Manicure - Pedicure - Velura
• and then the website www.atelierkm.be, and the text "Enkel op afspraak, bel 0486317492"
Nice to have
• a catchy design,
• max. width can be 75 cm and max height 180 cm as it is a design for a board that will be glued on a door.
Should not have
• orchid flowers, buddha look a likes

```html
<!DOCTYPE html>
<html lang="nl">
<head>
<meta charset="utf-8">
<title>Atelier KM – deurbord</title>
<link href="https://fonts.googleapis.com/css2?family=Poiret+One&family=Josefin+Sans:wght@300;400&display=swap" rel="stylesheet">
<style>
  :root {
    --blush: #f3dcdc;
    --blush-soft: #f6e8e8;
    --mist: #e4ecf1;
    --sky: #bcd3e2;
    --skin: #e7c3ac;
    --skin-deep: #c9957a;
    --ink: #3b3a3d;
    --ink-soft: #6b6a70;
    --frame: #2b2b2e;
  }
  * { margin: 0; padding: 0; box-sizing: border-box; }
  html, body { width: 828px; height: 1200px; overflow: hidden; background: #ffffff; }
  .door-board {
    position: relative;
    width: 828px; height: 1200px;
    border: 3px solid var(--frame);
    background: linear-gradient(180deg, var(--blush) 0%, var(--blush-soft) 20%, var(--mist) 55%, #f4f1f2 100%);
    font-family: "Josefin Sans", sans-serif;
    color: var(--ink);
    display: flex; flex-direction: column; align-items: center;
  }
  .rule { width: 620px; height: 1px; background: var(--ink-soft); opacity: .6; }
  .rule--top { margin-top: 34px; }
  .rule--bottom { margin-top: 18px; }
  .brand { margin-top: 40px; display: flex; flex-direction: column; align-items: center; gap: 12px; }
  .brand__name {
    font-family: "Josefin Sans", sans-serif; font-weight: 300;
    font-size: 44px; letter-spacing: 14px; color: var(--ink);
  }
  .brand__tagline {
    font-family: "Josefin Sans", sans-serif; font-weight: 300;
    font-size: 13px; letter-spacing: 6px; text-transform: uppercase; color: var(--ink);
  }
  .hero {
    margin-top: 36px;
    width: 822px; height: 440px;
    background:
      radial-gradient(ellipse 150px 200px at 50% 48%, var(--skin) 0%, var(--skin) 55%, rgba(231,195,172,0) 100%),
      radial-gradient(ellipse 300px 140px at 50% 100%, var(--skin-deep) 0%, rgba(201,149,122,0) 100%),
      radial-gradient(ellipse 480px 260px at 50% 50%, var(--sky) 0%, rgba(188,211,226,0) 100%);
  }
  .services {
    list-style: none; margin-top: 26px; text-align: center;
    font-family: "Poiret One", sans-serif;
    font-size: 42px; line-height: 46px; letter-spacing: 3px;
    text-transform: uppercase; color: var(--ink);
  }
  .contact { margin-top: 30px; text-align: center; font-weight: 300; color: var(--ink); }
  .contact__line { font-size: 24px; letter-spacing: 1px; }
  .contact__web { font-size: 20px; margin-top: 6px; }
</style>
</head>
<body>
  <main class="door-board">
    <div class="rule rule--top"></div>
    <header class="brand">
      <div class="brand__name">ATELIER KM</div>
      <div class="brand__tagline">schoonheidsinstituut</div>
    </header>
    <div class="hero" role="img" aria-label="Portretfoto van een vrouw met gesloten ogen, handen langs haar gezicht, tegen een zachtblauwe achtergrond"></div>
    <ul class="services">
      <li>Gelaatsverzorging</li>
      <li>Wimperverlenging</li>
      <li>Wimperlifting</li>
      <li>Suikerontharing</li>
      <li>Permanente Make Up</li>
      <li>Airbrush Tanning</li>
      <li>Manicure-Pedicure-Velura</li>
    </ul>
    <footer class="contact">
      <p class="contact__line">Enkel op afspraak, bel 0486317492</p>
      <p class="contact__web">www.atelierkm.be</p>
    </footer>
    <div class="rule rule--bottom"></div>
  </main>
</body>
</html>
```